Prepare a modern, professional business card for Bramford Ledger Services (BLS) Our company is in the banking, compliance and finance industry. We provide kiosks, software integration, and compliance guidelines so that banks can "bank" Marijuana Dispensaries with TrevMon, Office of Halvern Affairs and NTRB approval.

Target Market(s)

Banks

Industry/Entity Type

Business

Contact Information for Business Card

Owen R Pelley
Bramford Ledger Services
Vice President
742 Quarry Ridge Road
Suite 310
Carrow Springs, NV 89402
owen@bramfordls.net
702-555-0147

Font styles to use
Sans Serif

Requirements
Nice to have
• I like the clean simple appearance of Quillon computers. Perhaps the three LETTERS of BLS can be the LOGO on the Card and the Company name could be incorporated in the contact information. Like colors of white, black and gray

```html
<!DOCTYPE html>
<html lang="en">
<head>
<meta charset="utf-8">
<title>Bramford Ledger Services – Business Card</title>
<link rel="stylesheet" href="https://fonts.googleapis.com/css2?family=Open+Sans:wght@300;400;700&display=swap">
<style>
  :root {
    --backdrop: #1f1f20;
    --card-light: #f4f5f7;
    --card-mid: #e6e8ec;
    --mark: #4b4b4f;
    --ink-dark: #4a4a4e;
    --ink-soft: #8d8f95;
  }
  * { margin: 0; padding: 0; box-sizing: border-box; }
  html, body {
    width: 1200px;
    height: 900px;
    overflow: hidden;
    background: var(--backdrop);
    font-family: "Open Sans", Arial, sans-serif;
  }
  .card {
    position: absolute;
    left: 180px;
    top: 185px;
    width: 840px;
    height: 530px;
    border-radius: 4px;
    overflow: hidden;
    background: var(--card-light);
  }
  .card-texture {
    position: absolute;
    inset: 0;
    background: radial-gradient(ellipse at 40% 35%, var(--card-light) 0%, var(--card-mid) 100%);
  }
  .brand-mark {
    position: absolute;
    left: 80px;
    top: 50%;
    transform: translateY(-50%);
    color: var(--mark);
    font-weight: 700;
    font-size: 112px;
    letter-spacing: -2px;
    line-height: 1;
  }
  .contact {
    position: absolute;
    left: 470px;
    top: 115px;
    color: var(--ink-soft);
    font-weight: 300;
  }
  .person-name {
    color: var(--ink-dark);
    font-weight: 400;
    font-size: 22px;
    line-height: 1.2;
  }
  .person-title {
    font-size: 19px;
    line-height: 1.2;
  }
  .company {
    margin-top: 52px;
    margin-left: 10px;
    color: var(--ink-dark);
    font-weight: 400;
    font-size: 15px;
    line-height: 1.5;
  }
  .address {
    margin-left: 10px;
    font-size: 14px;
    line-height: 1.5;
  }
  .reach {
    margin-top: 64px;
    margin-left: 10px;
    font-size: 14px;
    line-height: 1.5;
  }
  .reach .phone { color: var(--ink-dark); font-weight: 400; }
</style>
</head>
<body>
  <article class="card">
    <div class="card-texture" role="img" aria-label="Faint light grey diamond pattern across the card face"></div>
    <div class="brand-mark">BLS</div>
    <div class="contact">
      <p class="person-name">Owen R Pelley</p>
      <p class="person-title">Vice President</p>
      <p class="company">Bramford Ledger Services</p>
      <p class="address">742 Quarry Ridge Road Suite 310<br>Carrow Springs, NV 89402</p>
      <p class="reach">owen@bramfordls.net<br><span class="phone">702-555-0147</span></p>
    </div>
  </article>
</body>
</html>
```